Falcrest security business card

Looking for a business card for my security company

Target Market(s)

Security

Industry/Entity Type

Security

Contact Information for Business Card

Name - Gil Marston. Title - General manager - direct 314 862.4490 website www. falcrestsecurityservices.example email - gil@ falcrestsecurityservices.example

Requirements
Must have
• Logo attached

```html
<!DOCTYPE html>
<html lang="en">
<head>
<meta charset="utf-8">
<title>Falcrest Security Services – Business Card</title>
<link rel="stylesheet" href="https://fonts.googleapis.com/css2?family=Montserrat:wght@700&family=Quicksand:wght@500;600&display=swap">
<style>
  :root {
    --backdrop: #1a1a1b;
    --card-dark: #161616;
    --card-light: #2e2e2f;
    --gold: #c9a35a;
    --gold-light: #f1dca6;
    --text-light: #f2f2f2;
  }
  * { margin: 0; padding: 0; box-sizing: border-box; }
  html, body {
    width: 1200px;
    height: 900px;
    overflow: hidden;
    background: var(--backdrop);
  }
  .stage {
    width: 1200px;
    height: 900px;
    display: flex;
    align-items: center;
    justify-content: center;
  }
  .business-card {
    position: relative;
    width: 1050px;
    height: 600px;
    background: radial-gradient(ellipse at 62% 40%, var(--card-light) 0%, var(--card-dark) 70%);
    overflow: hidden;
    box-shadow: 0 20px 50px rgba(0,0,0,0.6);
  }
  .accent-line {
    position: absolute;
    inset: 0;
  }
  .brand {
    position: absolute;
    left: 120px;
    top: 180px;
    display: flex;
    align-items: center;
    gap: 18px;
  }
  .brand-dot {
    width: 22px;
    height: 22px;
    border-radius: 50%;
    background: var(--gold);
  }
  .brand-name {
    font-family: "Montserrat", sans-serif;
    font-weight: 700;
    font-size: 78px;
    letter-spacing: 2px;
    text-transform: uppercase;
    color: var(--gold);
  }
  .contact-block {
    position: absolute;
    left: 440px;
    top: 360px;
  }
  .person-name {
    font-family: "Montserrat", sans-serif;
    font-weight: 700;
    font-size: 34px;
    letter-spacing: 1px;
    color: var(--gold);
    text-transform: uppercase;
  }
  .person-title {
    font-family: "Quicksand", sans-serif;
    font-weight: 500;
    font-size: 27px;
    color: var(--text-light);
    margin-top: 2px;
    margin-bottom: 20px;
  }
  .contact-list { list-style: none; }
  .contact-item {
    display: flex;
    align-items: center;
    gap: 16px;
    font-family: "Quicksand", sans-serif;
    font-weight: 500;
    font-size: 26px;
    color: var(--text-light);
    line-height: 40px;
  }
  .contact-icon {
    width: 24px;
    height: 24px;
    flex: none;
  }
</style>
</head>
<body>
<main class="stage">
  <section class="business-card">
    <svg class="accent-line" width="1050" height="600" viewBox="0 0 1050 600" aria-hidden="true">
      <defs>
        <linearGradient id="goldStroke" x1="0" y1="0" x2="1" y2="0">
          <stop offset="0" stop-color="#b48a45"/>
          <stop offset="0.5" stop-color="#e6c987"/>
          <stop offset="1" stop-color="#b48a45"/>
        </linearGradient>
      </defs>
      <polyline points="0,150 80,150 80,310 1050,310" fill="none" stroke="url(#goldStroke)" stroke-width="5"/>
      <g class="rank-stars">
        <rect x="838" y="292" width="170" height="36" fill="#1c1c1c"/>
        <polygon fill="var(--gold)" transform="translate(860 310) scale(0.9)"
          points="0,-18 5.3,-6 18,-5.6 8.5,3 11.2,16 0,9 -11.2,16 -8.5,3 -18,-5.6 -5.3,-6"/>
        <polygon fill="var(--gold-light)" transform="translate(923 310) scale(1.35)"
          points="0,-18 5.3,-6 18,-5.6 8.5,3 11.2,16 0,9 -11.2,16 -8.5,3 -18,-5.6 -5.3,-6"/>
        <polygon fill="var(--gold)" transform="translate(986 310) scale(0.9)"
          points="0,-18 5.3,-6 18,-5.6 8.5,3 11.2,16 0,9 -11.2,16 -8.5,3 -18,-5.6 -5.3,-6"/>
      </g>
    </svg>

    <div class="brand">
      <span class="brand-dot"></span>
      <span class="brand-name">Falcrest</span>
    </div>

    <div class="contact-block">
      <h1 class="person-name">Gil Marston</h1>
      <p class="person-title">General manager</p>
      <ul class="contact-list">
        <li class="contact-item">
          <svg class="contact-icon" viewBox="0 0 24 24" aria-hidden="true">
            <circle cx="12" cy="12" r="12" fill="var(--gold)"/>
            <path d="M8 6.5h2.2l1 3-1.4 1a7 7 0 0 0 3.7 3.7l1-1.4 3 1v2.2a1.5 1.5 0 0 1-1.6 1.5A10.5 10.5 0 0 1 6.5 8.1 1.5 1.5 0 0 1 8 6.5z" fill="#1b1b1b"/>
          </svg>
          <span>314 862.4490</span>
        </li>
        <li class="contact-item">
          <svg class="contact-icon" viewBox="0 0 24 24" aria-hidden="true">
            <circle cx="12" cy="12" r="12" fill="var(--gold)"/>
            <rect x="6" y="8" width="12" height="8.5" rx="1" fill="none" stroke="#1b1b1b" stroke-width="1.6"/>
            <polyline points="6.5,8.8 12,13 17.5,8.8" fill="none" stroke="#1b1b1b" stroke-width="1.6"/>
          </svg>
          <span>gil@falcrestsecurityservices.example</span>
        </li>
        <li class="contact-item">
          <svg class="contact-icon" viewBox="0 0 24 24" aria-hidden="true">
            <circle cx="12" cy="12" r="12" fill="var(--gold)"/>
            <circle cx="12" cy="12" r="6" fill="none" stroke="#1b1b1b" stroke-width="1.5"/>
            <ellipse cx="12" cy="12" rx="2.6" ry="6" fill="none" stroke="#1b1b1b" stroke-width="1.3"/>
            <line x1="6" y1="12" x2="18" y2="12" stroke="#1b1b1b" stroke-width="1.3"/>
          </svg>
          <span>falcrestsecurityservices.example</span>
        </li>
      </ul>
    </div>
  </section>
</main>
</body>
</html>
```